Printed Promo Flyer for new pet business

We need a double sided flyer design as per the given example flyer, just better looking and more fun.Flyers will need to be printed.Flyer size approx 10.5cm x 15cm. The text will need to be amended slightly afterwards to be more fun unless you can create a new tone of voice as well (should sound fun like breezy do it) Look and Feel: emotional, fun, loving, professional
See attached files.

Target Market(s)

Pet owners in the UK who want the convenience of getting their pets parasite treatment delivered to their door without the need of having to run to the vet or store for purchase

Industry/Entity Type

Pet Care

Colors
00a990
6b449b

Requirements
Must have
• all the content context as given in the example flyer.
Nice to have
• Tone of voice can be changed to be more fun (using Breezy as a guide)

```html
<!DOCTYPE html>
<html lang="en">
<head>
<meta charset="utf-8">
<title>Paw Parcel – Promo Flyer</title>
<link href="https://fonts.googleapis.com/css2?family=Roboto+Slab:wght@700&family=Montserrat:wght@500;700&display=swap" rel="stylesheet">
<style>
  :root{
    --stage:#474556;
    --paper:#e9dfd3;
    --paper-light:#f2ebe2;
    --teal:#00a8b5;
    --purple:#6b449b;
    --white:#ffffff;
    --ink:#2b2430;
    --art-grey:#b9b8bd;
    --art-orange:#e8a43e;
    --slab:'Roboto Slab', Georgia, serif;
    --sans:'Montserrat', Arial, sans-serif;
  }
  *{box-sizing:border-box;margin:0;padding:0}
  html,body{width:1200px;height:3600px;overflow:hidden;background:var(--stage)}
  .stage{position:relative;width:1200px;height:3600px}
  .page{
    position:absolute;left:192px;width:817px;height:1167px;overflow:hidden;
    background:radial-gradient(ellipse at 30% 30%,var(--paper-light),var(--paper) 70%);
  }
  .page--front{top:583px}
  .page--back{top:1850px}
  .abs{position:absolute}
  .brand{
    position:absolute;font-family:var(--slab);font-weight:700;color:var(--purple);
    letter-spacing:2px;white-space:nowrap;
  }
  .svg-layer{position:absolute;left:0;top:0}

  /* front */
  .front-brand{left:0;width:817px;text-align:center;top:150px;font-size:56px}
  .hero-circle{left:97px;top:276px;width:630px;height:630px;border-radius:50%;background:var(--teal)}
  .hero-kicker{left:0;width:817px;text-align:center;top:408px;font-family:var(--slab);font-weight:700;color:var(--white);font-size:40px;line-height:50px}
  .hero-title{left:0;width:817px;text-align:center;top:510px;font-family:var(--slab);font-weight:700;color:var(--white);font-size:104px;line-height:110px;white-space:nowrap}
  .pets-art{
    left:205px;top:640px;width:420px;height:390px;border-radius:18px;
    background:linear-gradient(135deg,var(--art-grey) 0%,var(--art-orange) 55%,var(--purple) 100%);
    opacity:.85;
  }
  .front-tagline{left:0;width:817px;text-align:center;top:1078px;font-family:var(--slab);font-weight:700;color:var(--teal);font-size:42px;white-space:nowrap}

  /* back */
  .why-blob{left:-130px;top:-160px;width:374px;height:409px;border-radius:50%;background:var(--purple)}
  .why-title{left:40px;top:68px;font-family:var(--slab);font-weight:700;color:var(--white);font-size:64px}
  .why-pill{left:242px;top:78px;height:46px;padding:0 22px 0 12px;border-radius:0 23px 23px 0;background:var(--teal);
    font-family:var(--slab);font-weight:700;color:var(--white);font-size:26px;line-height:46px;white-space:nowrap}
  .back-brand{left:500px;top:146px;width:300px;text-align:center;font-size:34px}

  .features{position:absolute;left:40px;top:280px;list-style:none}
  .feature{position:relative;height:147px;padding-left:125px}
  .feature-icon{position:absolute;left:0;top:12px;width:94px;height:94px;border-radius:50%;background:var(--teal);
    display:flex;align-items:center;justify-content:center}
  .feature-ring{position:absolute;left:-12px;top:0;width:118px;height:118px}
  .feature-title{font-family:var(--slab);font-weight:700;font-size:25px;color:var(--teal);line-height:32px;white-space:nowrap}
  .feature-title--purple{color:var(--purple)}
  .feature-text{font-family:var(--sans);font-weight:500;font-size:20px;line-height:25px;color:var(--ink);white-space:nowrap}

  .offer-disc{left:512px;top:374px;width:336px;height:336px;border-radius:50%;background:var(--white)}
  .offer-label{left:512px;width:310px;top:438px;text-align:center;font-family:var(--slab);font-weight:700;color:var(--purple);font-size:28px}
  .offer-price{left:512px;width:310px;top:470px;text-align:center;font-family:var(--slab);font-weight:700;color:var(--teal);font-size:72px}
  .offer-code-label{left:512px;width:310px;top:568px;text-align:center;font-family:var(--sans);font-weight:700;color:var(--ink);font-size:15px}
  .offer-code{left:567px;top:598px;width:201px;height:32px;border:2px solid var(--purple);text-align:center;
    font-family:var(--sans);font-weight:500;color:var(--purple);font-size:24px;line-height:28px}

  .steps-frame{left:119px;top:881px;width:586px;height:248px;border:2px solid var(--purple)}
  .steps-pill{left:258px;top:849px;height:58px;display:flex;border-radius:29px;overflow:hidden;white-space:nowrap;
    font-family:var(--slab);font-weight:700;color:var(--white);font-size:28px;line-height:58px}
  .steps-pill span:first-child{background:var(--purple);padding:0 10px 0 30px}
  .steps-pill span:last-child{background:var(--teal);padding:0 28px 0 12px}
  .step{position:absolute;display:flex;align-items:center;gap:16px}
  .step-num{width:54px;height:54px;border-radius:6px;background:var(--purple);color:var(--white);
    font-family:var(--slab);font-weight:700;font-size:38px;line-height:54px;text-align:center;flex:none}
  .step-text{font-family:var(--sans);font-weight:500;font-size:19px;line-height:23px;color:var(--ink);white-space:nowrap}
</style>
</head>
<body>
<main class="stage">

  <!-- Front side -->
  <section class="page page--front" aria-label="Flyer front">
    <div class="brand front-brand">PAW PARCEL</div>
    <div class="abs hero-circle"></div>
    <svg class="svg-layer" width="817" height="1167" aria-hidden="true">
      <path d="M172 364 A335 335 0 0 0 168 835" fill="none" stroke="var(--purple)" stroke-width="12" stroke-linecap="round" stroke-dasharray="0 18"/>
      <path d="M680 434 A335 335 0 0 1 615 835" fill="none" stroke="var(--white)" stroke-width="12" stroke-linecap="round" stroke-dasharray="0 18"/>
    </svg>
    <p class="abs hero-kicker">BEST PROTECTION<br>&amp; CARE FOR</p>
    <h1 class="abs hero-title">YOUR PET</h1>
    <div class="abs pets-art" role="img" aria-label="Illustration placeholder: a grey cat and an orange dog sitting together on a purple mat"></div>
    <p class="abs front-tagline">WITH PAW PARCEL</p>
  </section>

  <!-- Back side -->
  <section class="page page--back" aria-label="Flyer back">
    <div class="abs why-blob"></div>
    <svg class="svg-layer" width="817" height="1167" aria-hidden="true">
      <line x1="8" y1="228" x2="100" y2="228" stroke="var(--white)" stroke-width="4" stroke-linecap="round" stroke-dasharray="0 8"/>
      <path d="M518 470 A193 193 0 0 1 830 390" fill="none" stroke="var(--teal)" stroke-width="3"/>
      <path d="M498 560 A185 185 0 0 0 830 700" fill="none" stroke="var(--purple)" stroke-width="3"/>
      <path d="M540 520 A150 150 0 0 0 830 660" fill="none" stroke="var(--teal)" stroke-width="3"/>
    </svg>
    <h2 class="abs why-title">WHY</h2>
    <div class="abs why-pill">PAW PARCEL?</div>
    <div class="brand back-brand">PAW PARCEL</div>

    <ul class="features">
      <li class="feature">
        <svg class="feature-ring" viewBox="0 0 118 118" aria-hidden="true"><path d="M59 4 A55 55 0 0 1 59 114" fill="none" stroke="var(--purple)" stroke-width="4" stroke-linecap="round" stroke-dasharray="0 8"/></svg>
        <div class="feature-icon"><svg width="48" height="48" viewBox="0 0 24 24" aria-hidden="true"><path d="M12 21 3.5 12.5A5 5 0 0 1 12 5.5a5 5 0 0 1 8.5 7Z" fill="none" stroke="var(--white)" stroke-width="2" stroke-linejoin="round"/></svg></div>
        <h3 class="feature-title feature-title--purple">PROTECTION &amp; CARE</h3>
        <p class="feature-text">Protection against all major<br>parasites to avoid putting your<br>pet and your family at risk</p>
      </li>
      <li class="feature">
        <svg class="feature-ring" viewBox="0 0 118 118" aria-hidden="true"><path d="M59 4 A55 55 0 0 1 59 114" fill="none" stroke="var(--purple)" stroke-width="4" stroke-linecap="round" stroke-dasharray="0 8"/></svg>
        <div class="feature-icon"><svg width="48" height="48" viewBox="0 0 24 24" aria-hidden="true"><circle cx="12" cy="12" r="9" fill="none" stroke="var(--white)" stroke-width="2"/><path d="M12 7v5l3 2" fill="none" stroke="var(--white)" stroke-width="2" stroke-linecap="round"/></svg></div>
        <h3 class="feature-title">IN TIME</h3>
        <p class="feature-text">Never having to remember<br>when to treat your pet</p>
      </li>
      <li class="feature">
        <svg class="feature-ring" viewBox="0 0 118 118" aria-hidden="true"><path d="M59 4 A55 55 0 0 1 59 114" fill="none" stroke="var(--purple)" stroke-width="4" stroke-linecap="round" stroke-dasharray="0 8"/></svg>
        <div class="feature-icon"><svg width="48" height="48" viewBox="0 0 24 24" aria-hidden="true"><path d="M12 3 20 7v10l-8 4-8-4V7Zm0 8 8-4M12 11 4 7m8 4v10" fill="none" stroke="var(--white)" stroke-width="2" stroke-linejoin="round"/></svg></div>
        <h3 class="feature-title">CONVENIENT</h3>
        <p class="feature-text">Delivered directly to your<br>letter box</p>
      </li>
      <li class="feature">
        <svg class="feature-ring" viewBox="0 0 118 118" aria-hidden="true"><path d="M59 4 A55 55 0 0 1 59 114" fill="none" stroke="var(--purple)" stroke-width="4" stroke-linecap="round" stroke-dasharray="0 8"/></svg>
        <div class="feature-icon"><svg width="50" height="50" viewBox="0 0 24 24" aria-hidden="true"><rect x="2" y="6" width="20" height="12" rx="1.5" fill="none" stroke="var(--white)" stroke-width="2"/><circle cx="12" cy="12" r="3" fill="none" stroke="var(--white)" stroke-width="2"/></svg></div>
        <h3 class="feature-title">LOW COST</h3>
        <p class="feature-text">All the high end, trusted brands<br>but cheaper than the vet</p>
      </li>
    </ul>

    <div class="abs offer-disc"></div>
    <p class="abs offer-label">FIRST BOX</p>
    <p class="abs offer-price">£5.99</p>
    <p class="abs offer-code-label">USE CODE</p>
    <div class="abs offer-code">XXX</div>

    <div class="abs steps-frame"></div>
    <div class="abs steps-pill"><span>HOW IT</span><span>WORKS</span></div>
    <div class="step" style="left:164px;top:943px"><span class="step-num">1</span><span class="step-text">Select which pet<br>the treatment is for</span></div>
    <div class="step" style="left:435px;top:932px"><span class="step-num">3</span><span class="step-text">Select your<br>preferred brand</span></div>
    <div class="step" style="left:164px;top:1037px"><span class="step-num">2</span><span class="step-text">Choose your<br>treatment type</span></div>
    <div class="step" style="left:435px;top:1036px"><span class="step-num">4</span><span class="step-text">Choose between<br>1, 3, 6 or 12 months<br>treatment box</span></div>
  </section>

</main>
</body>
</html>
```